QPM Habitat Helpers 2019

We need a 2 page flyer to advertise our upcoming program. The program covers 5 months May-September 2019 and is focused on conservation.I have attached some options that i like. It needs to be striking.

Text in newly uploaded document 'HHFlyer2'

Target Market(s)

Conservation
Conscious travelers
30-45 year olds
Environmental
Adventure/Hiking
Citizen Science

Font styles to use
Sans Serif

Colors
0355a3
fbed22

Requirements
Must have
• A travel conservation focus
• Highlight the significance of the 'in the world' status of the project
Nice to have
• A yellow border, making it look similar to the cover of Wandering Horizons

```html
<!DOCTYPE html>
<html lang="en">
<head>
<meta charset="utf-8">
<title>QPM Habitat Helpers – In The World 2019</title>
<link href="https://fonts.googleapis.com/css2?family=Montserrat:wght@400;500;600&family=Satisfy&family=Noto+Serif:wght@400&display=swap" rel="stylesheet">
<style>
  :root {
    --brand-blue: #0355a3;
    --brand-yellow: #fbed22;
    --sky: #3c86e0;
    --ocean-light: #2f9fd0;
    --ocean-deep: #0d3b74;
    --ocean-dark: #0a2b55;
    --foliage: #2e5a2a;
    --ink-white: #ffffff;
    --ice-blue: #cfe9ff;
    --backdrop: #ececec;
  }
  html, body {
    margin: 0;
    padding: 0;
    width: 1200px;
    height: 986px;
    overflow: hidden;
    background: var(--backdrop);
  }
  .canvas {
    position: relative;
    width: 1200px;
    height: 986px;
  }
  .flyer {
    position: absolute;
    left: 268px;
    top: 23px;
    width: 664px;
    height: 940px;
    overflow: hidden;
    background: var(--ocean-deep);
    box-shadow: 0 8px 24px rgba(0,0,0,0.18);
    font-family: "Montserrat", sans-serif;
    color: var(--ink-white);
  }
  .flyer__photo {
    position: absolute;
    inset: 0;
    background:
      radial-gradient(ellipse 55% 45% at 95% 88%, var(--foliage) 0%, rgba(46,90,42,0.6) 45%, rgba(46,90,42,0) 75%),
      radial-gradient(ellipse 40% 12% at 75% 24%, rgba(120,150,90,0.7) 0%, rgba(120,150,90,0) 100%),
      linear-gradient(180deg, var(--sky) 0%, #6aa8e6 14%, var(--ocean-light) 24%, #1b63a8 38%, var(--ocean-deep) 62%, var(--ocean-dark) 100%);
  }
  .flyer__border-top {
    position: absolute;
    left: 0;
    top: 0;
    width: 100%;
    height: 34px;
    background: var(--brand-yellow);
  }
  .flyer__border-left {
    position: absolute;
    left: 0;
    top: 0;
    width: 34px;
    height: 62%;
    background: linear-gradient(180deg, var(--brand-yellow) 0%, var(--brand-yellow) 60%, rgba(251,237,34,0) 100%);
  }
  .brand {
    position: absolute;
    left: 120px;
    top: 70px;
    display: flex;
    align-items: center;
    gap: 10px;
  }
  .brand__dot {
    width: 18px;
    height: 18px;
    border-radius: 50%;
    background: var(--ink-white);
  }
  .brand__name {
    font-weight: 600;
    font-size: 17px;
    letter-spacing: 1px;
    color: var(--ink-white);
    text-transform: uppercase;
  }
  .title-frame {
    position: absolute;
    left: 78px;
    top: 262px;
    width: 512px;
    height: 208px;
    border: 1.5px solid rgba(255,255,255,0.9);
  }
  .title__lead {
    position: absolute;
    left: 96px;
    top: 232px;
    font-weight: 500;
    font-size: 50px;
    letter-spacing: 2px;
    line-height: 1;
  }
  .title__main {
    position: absolute;
    left: 130px;
    top: 268px;
    font-family: "Satisfy", cursive;
    font-size: 160px;
    line-height: 1;
  }
  .tagline {
    position: absolute;
    left: 0;
    width: 100%;
    top: 500px;
    text-align: center;
    font-weight: 400;
    font-size: 34px;
    letter-spacing: 4px;
    color: var(--ice-blue);
  }
  .dates {
    position: absolute;
    left: 50%;
    top: 572px;
    transform: translateX(-50%);
    padding: 10px 22px;
    border: 1.5px solid rgba(255,255,255,0.7);
    font-weight: 500;
    font-size: 30px;
    letter-spacing: 3px;
    white-space: nowrap;
  }
  .year {
    position: absolute;
    left: 0;
    width: 100%;
    top: 650px;
    text-align: center;
    font-weight: 500;
    font-size: 62px;
    letter-spacing: 4px;
  }
  .web-tag {
    position: absolute;
    right: 40px;
    bottom: 48px;
    padding: 8px 26px;
    background: var(--brand-yellow);
    color: #1a1a1a;
    font-family: "Noto Serif", serif;
    font-size: 20px;
    letter-spacing: 1px;
  }
</style>
</head>
<body>
<main class="canvas">
  <article class="flyer">
    <div class="flyer__photo" role="img" aria-label="Aerial photograph of a tropical island coastline with turquoise lagoon, deep blue ocean and palm-covered shore"></div>
    <div class="flyer__border-top"></div>
    <div class="flyer__border-left"></div>

    <div class="brand">
      <span class="brand__dot"></span>
      <span class="brand__name">QPM Habitat Helpers</span>
    </div>

    <div class="title-frame"></div>
    <h1 class="title__lead" style="margin:0">IN THE</h1>
    <div class="title__main">World</div>

    <p class="tagline" style="margin:0">TRAVEL CONSERVATION</p>
    <div class="dates">MAY-SEPTEMBER</div>
    <p class="year" style="margin:0">2019</p>

    <div class="web-tag">www.yourwebsite.com</div>
  </article>
</main>
</body>
</html>
```